Community grantmaker building brochure site

The Kelvora Community Trust is a grant-making agency that seeks to build an emotionally engaging and informative site that portrays Haiti from an asset lens. We want to focus on the opportunities for growth while highlighting the current opportunity to give to a worthy cause.

Users will be Haitians, Allies of Lantos, and Media who are potential donors, innovators and decision makers.

We envision a home page with a horizontal navigation bar (with About us, Impact/Our work/Projects, Donate, Contact us, Meet the team, and Haiti’s assets/facts/resources/research) a series of large horizontal images (with dissolving motion) and language underneath the image that describes who we are and what we do.

We currently have content for the tabs below:

About us: Kelvora Community Trust - The Trust is the country’s first endowed fund building on Haiti’s assets while providing resources for scalable solutions.

The Trust addresses three essential pillars for a thriving Kelvora: environment, entrepreneurship, and civic education. We will invest in water resources focusing in an integrative and systemic way on the lasting impact of this approach.

Donate: A link to the Brandel Foundation and statement about Hurricane Dorvell. “Giving for Outcomes”

Sustainable Funding: Links to articles and resources that show our theory of change while highlighting facts about Haiti.

Meet the team: A list of names and images of the board

Also in the same frame we would like 3 tiles titled The Environment, Entrepreneurship, Civic Engagement with an option to scroll over for additional information.

Lastly the link to donate should be featured prominently and several times along with cues that lead people to find out more about the facts and the Sustainable Funding page.

We prefer limited scrolling and would like to see a clean yet modern approach to this funding platform.

Thank you and looking forward!
Updates

Reason: Thank you! Our executive board has rescheduled our meeting so we'll need a few more days to coordinate. Much appreciated.

Target Market(s)

Haitians, Allies of Lantos, and Media who are potential donors, innovators and decision makers

Industry/Entity Type

Foundation

Coding

Coded - Design and coding required

Number of Pages Required

5+ page

Requirements
Must have
• emotionally engaging and informative
• asset-focused language
• motion enabled pictures
• links to donate
Nice to have
• scoll-over and pop-ups
• music
Should not have
• charity language
• denigrating language
• images that depict poverty or need

```html
<!DOCTYPE html>
<html lang="en">
<head>
<meta charset="utf-8">
<title>Kelvora Community Trust</title>
<link href="https://fonts.googleapis.com/css2?family=Roboto+Slab:wght@400;700&family=Roboto+Condensed:wght@400;700&family=Roboto:wght@400;500&display=swap" rel="stylesheet">
<style>
:root{
  --red:#c8202f;
  --blue:#1f4a8f;
  --ink:#333333;
  --text:#5a5a5a;
  --muted:#8a8a8a;
  --nav:#323232;
  --light:#f0f0f0;
  --line:#e2e2e2;
  --bar:#a6a6a6;
  --white:#ffffff;
}
*{box-sizing:border-box;margin:0;padding:0}
html,body{width:1200px;height:2941px;overflow:hidden;background:var(--white)}
body{font-family:"Roboto",Arial,sans-serif;color:var(--text);position:relative}
.slab{font-family:"Roboto Slab",Georgia,serif}
.abs{position:absolute}

/* header */
.site-header{position:absolute;left:0;top:0;width:1200px;height:92px}
.brand{position:absolute;left:98px;top:20px;display:flex;align-items:center;gap:12px}
.brand-dot{width:48px;height:48px;border-radius:50%;border:2px solid var(--red)}
.brand-name{font-family:"Roboto Condensed",sans-serif;font-weight:700;font-size:26px;color:var(--red);letter-spacing:.5px;text-transform:uppercase}
.header-contact{position:absolute;top:34px;font-size:14px;color:var(--ink);display:flex;align-items:center;gap:8px}
.header-contact svg{width:14px;height:14px}
.search-btn{position:absolute;left:1057px;top:26px;width:40px;height:40px;border-radius:50%;background:#f2f2f2;display:flex;align-items:center;justify-content:center}

/* nav */
.main-nav{position:absolute;left:0;top:92px;width:1200px;height:67px;background:var(--nav)}
.main-nav a{position:absolute;top:0;height:67px;line-height:67px;color:var(--white);font-family:"Roboto Condensed",sans-serif;font-size:15px;text-decoration:none;text-transform:uppercase;text-align:center}
.main-nav a.active{background:var(--red);left:98px;width:100px}

/* hero */
.hero{position:absolute;left:0;top:159px;width:1200px;height:513px;background:linear-gradient(180deg,#8aa06a 0%,#4f7a3a 45%,#2f5a26 100%)}
.hero-title{position:absolute;left:0;width:1200px;top:240px;text-align:center;font-family:"Roboto Condensed",sans-serif;font-weight:700;font-size:54px;color:var(--white)}
.hero-sub{position:absolute;left:300px;width:600px;top:318px;text-align:center;font-family:"Roboto Slab",serif;font-size:18px;line-height:28px;color:var(--white)}
.hero-btn{position:absolute;left:498px;top:396px;width:202px;height:59px;border-radius:8px;background:var(--red);color:var(--white);font-family:"Roboto Condensed",sans-serif;font-weight:700;font-size:22px;line-height:59px;text-align:center}
.hero-arrow{position:absolute;top:210px;width:30px;height:60px}

/* section titles */
.sec-title{position:absolute;left:0;width:1200px;text-align:center;font-family:"Roboto Slab",serif;font-size:28px;color:var(--ink);text-transform:uppercase}
.sec-lead{position:absolute;left:200px;width:800px;text-align:center;font-size:13px;line-height:22px;color:var(--text)}

/* welcome */
.pillar{position:absolute;top:839px;width:320px;height:100px}
.pillar-icon{position:absolute;left:0;top:0;width:94px;height:94px}
.pillar h3{position:absolute;left:106px;top:16px;font-family:"Roboto Slab",serif;font-weight:400;font-size:18px;color:var(--ink);text-transform:uppercase}
.pillar p{position:absolute;left:106px;top:48px;width:210px;font-size:13px;line-height:20px;color:var(--text)}

/* about */
.about{position:absolute;left:0;top:1029px;width:1200px;height:369px}
.about-text{position:absolute;left:0;top:0;width:606px;height:369px;background:var(--light)}
.about-text h2{position:absolute;left:98px;top:36px;font-family:"Roboto Slab",serif;font-weight:400;font-size:28px;color:var(--ink)}
.about-text p{position:absolute;left:98px;top:92px;width:470px;font-size:13px;line-height:23px;color:var(--text)}
.btn-blue{position:absolute;left:98px;top:274px;width:110px;height:40px;background:var(--blue);color:var(--white);font-size:11px;font-weight:500;line-height:40px;text-align:center;text-transform:uppercase}
.about-photo{position:absolute;left:606px;top:0;width:594px;height:369px;background:radial-gradient(circle at 60% 30%,#e4cf96 0%,#a9845a 40%,#3c3124 100%)}

/* what we do */
.card{position:absolute;top:1592px;width:320px;height:388px;background:var(--white);border:1px solid var(--line);box-shadow:0 12px 14px -8px rgba(0,0,0,.25)}
.card-photo{position:absolute;left:15px;top:15px;width:290px;height:169px}
.card h3{position:absolute;left:0;width:100%;top:216px;text-align:center;font-family:"Roboto Slab",serif;font-weight:400;font-size:17px;color:var(--ink);text-transform:uppercase}
.card p{position:absolute;left:20px;width:280px;top:254px;text-align:center;font-size:12px;line-height:20px;color:var(--text)}
.btn-red{position:absolute;left:106px;top:352px;width:108px;height:36px;background:var(--red);color:var(--white);font-size:11px;font-weight:500;line-height:36px;text-align:center;text-transform:uppercase}

/* team */
.team{position:absolute;left:0;top:2054px;width:1200px;height:480px;background:linear-gradient(135deg,#22344e 0%,#3d5675 45%,#2a3d58 100%)}
.team .sec-title{color:var(--white);top:36px}
.team .sec-lead{color:var(--white);top:90px}
.member{position:absolute;text-align:center;color:var(--white)}
.member-photo{border-radius:50%;border:4px solid var(--white);margin:0 auto}
.member-name{font-family:"Roboto Slab",serif;font-size:19px;margin-top:14px}
.member-role{font-size:12px;margin-top:4px}
.team-arrow{position:absolute;top:256px;width:20px;height:40px}

/* footer */
.footer-col{position:absolute;top:2610px}
.footer-col h4{font-family:"Roboto Slab",serif;font-weight:400;font-size:18px;color:var(--ink);text-transform:uppercase;padding-bottom:10px;position:relative}
.footer-col h4::after{content:"";position:absolute;left:0;bottom:0;width:30px;height:2px;background:var(--blue)}
.footer-col ul{list-style:none;margin-top:18px}
.footer-col li{font-size:12px;color:var(--text);height:45px;line-height:40px;border-bottom:1px solid var(--line);width:150px}
.contact li{width:195px;height:auto;line-height:20px;padding:8px 0}
.newsletter p{width:300px;font-size:12px;line-height:20px;margin-top:20px}
.signup{display:flex;margin-top:18px}
.signup .field{width:250px;height:44px;border:1px solid var(--line);font-size:11px;color:var(--muted);line-height:42px;padding-left:14px}
.signup .send{width:44px;height:44px;background:var(--blue);display:flex;align-items:center;justify-content:center}
.social{display:flex;gap:12px;margin-top:18px}
.social span{width:32px;height:32px;border-radius:50%;border:2px solid var(--white);box-shadow:0 0 0 1px var(--line)}
.bottom-bar{position:absolute;left:0;top:2879px;width:1200px;height:62px;background:var(--bar);color:var(--white);font-size:12px}
.bottom-bar .copy{position:absolute;left:98px;top:23px}
.bottom-bar nav{position:absolute;right:98px;top:23px;display:flex;gap:36px}
</style>
</head>
<body>

<header class="site-header">
  <div class="brand"><span class="brand-dot"></span><span class="brand-name">Kelvora Community Trust</span></div>
  <div class="header-contact" style="left:672px">
    <svg viewBox="0 0 14 14"><rect x="1" y="3" width="12" height="9" rx="1" fill="none" stroke="#1f4a8f" stroke-width="1.5"/><path d="M1 4l6 4 6-4" fill="none" stroke="#1f4a8f" stroke-width="1.5"/></svg>
    info@kelvoracommunitytrust.com
  </div>
  <div class="header-contact" style="left:930px">
    <svg viewBox="0 0 14 14"><path d="M3 1l3 3-2 2c1 2 2 3 4 4l2-2 3 3-2 2C6 13 1 8 1 3z" fill="#1f4a8f"/></svg>
    123 456 7895
  </div>
  <div class="search-btn"><svg width="16" height="16" viewBox="0 0 16 16"><circle cx="6.5" cy="6.5" r="5" fill="none" stroke="#1f4a8f" stroke-width="2"/><path d="M10 10l5 5" stroke="#1f4a8f" stroke-width="2"/></svg></div>
</header>

<nav class="main-nav">
  <a class="active" href="#">Home</a>
  <a href="#" style="left:220px;width:115px">About Us</a>
  <a href="#" style="left:360px;width:110px">Our Work</a>
  <a href="#" style="left:500px;width:100px">Donate</a>
  <a href="#" style="left:630px;width:130px">Contact Us</a>
  <a href="#" style="left:795px;width:150px">Meet the Team</a>
  <a href="#" style="left:975px;width:130px">Haiti's Assets</a>
</nav>

<section class="hero" role="img" aria-label="Smiling man with open arms standing in a field of tall green sugar cane">
  <svg class="hero-arrow" style="left:72px" viewBox="0 0 30 60"><path d="M22 10L8 30l14 20" fill="none" stroke="#fff" stroke-width="3"/></svg>
  <svg class="hero-arrow" style="left:1098px" viewBox="0 0 30 60"><path d="M8 10l14 20L8 50" fill="none" stroke="#fff" stroke-width="3"/></svg>
  <h1 class="hero-title">KELVORA COMMUNITY TRUST</h1>
  <p class="hero-sub">Grant-making agency that seeks to build an emotionally engaging and informative site that portrays Haiti from an asset lens</p>
  <a class="hero-btn">DONATE NOW!</a>
</section>

<section class="welcome">
  <h2 class="sec-title" style="top:710px">Welcome!</h2>
  <p class="sec-lead" style="top:752px;left:190px;width:820px">Pleasure and praising pain was born and I will give you a complete account of the system, and expound the actual teachings of the great explorer of the truth, the master-builder of human happiness. No one rejects, dislikes, or avoids pleasure itself.</p>

  <div class="pillar" style="left:98px">
    <svg class="pillar-icon" viewBox="0 0 94 94"><circle cx="47" cy="47" r="47" fill="#c8202f"/><circle cx="47" cy="47" r="35" fill="#fff"/><circle cx="47" cy="47" r="29" fill="#1f4a8f"/><path d="M36 58c0-14 8-22 22-24-2 14-10 22-22 24zM36 58l12-12" fill="#fff" stroke="#fff" stroke-width="2"/></svg>
    <h3>Environment</h3>
    <p>Praesentium voluptatum deleniti atque corrupti quos dolores</p>
  </div>
  <div class="pillar" style="left:451px">
    <svg class="pillar-icon" viewBox="0 0 94 94"><circle cx="47" cy="47" r="47" fill="#c8202f"/><circle cx="47" cy="47" r="35" fill="#fff"/><circle cx="47" cy="47" r="29" fill="#1f4a8f"/><circle cx="47" cy="43" r="9" fill="#fff"/><rect x="43" y="52" width="8" height="7" fill="#fff"/><path d="M47 26v4M33 32l3 3M61 32l-3 3M29 44h4M61 44h4" stroke="#fff" stroke-width="2"/></svg>
    <h3>Entrepreneurship</h3>
    <p>Praesentium voluptatum deleniti atque corrupti quos dolores</p>
  </div>
  <div class="pillar" style="left:802px">
    <svg class="pillar-icon" viewBox="0 0 94 94"><circle cx="47" cy="47" r="47" fill="#c8202f"/><circle cx="47" cy="47" r="35" fill="#fff"/><circle cx="47" cy="47" r="29" fill="#1f4a8f"/><path d="M28 42l19-9 19 9-19 9z" fill="#fff"/><path d="M36 46v9c6 4 16 4 22 0v-9l-11 5z" fill="#fff"/><path d="M64 43v10" stroke="#fff" stroke-width="2"/></svg>
    <h3>Civic Education</h3>
    <p>Praesentium voluptatum deleniti atque corrupti quos dolores</p>
  </div>
</section>

<section class="about">
  <div class="about-text">
    <h2>ABOUT US</h2>
    <p>Praising pain was born and I will give you a complete account of the system, and expound the actual teachings of the great explorer of the truth, the master-builder of human happiness. No one rejects, dislikes, or avoids pleasure itself, because it is pleasure, but because those who do not know how to pursue pleasure rationally encounter consequences that are extremely painful. Nor again is there anyone who loves or pursues or desires to obtain pain of itself, because it is pain, but because occasionally circumstances occur in which toil and pain.</p>
    <a class="btn-blue">Learn More</a>
  </div>
  <div class="about-photo" role="img" aria-label="Cupped hands holding soil with a young green seedling"></div>
</section>

<section class="what-we-do">
  <h2 class="sec-title" style="top:1456px">What We Do!</h2>
  <p class="sec-lead" style="top:1506px">There are many variations of passages of Lorem Ipsum available, but the majority have suffered alteration in some form, by injected humour, or randomised words which don't look even slightly believable.</p>

  <article class="card" style="left:98px">
    <div class="card-photo" role="img" aria-label="Students writing at desks in an outdoor classroom" style="background:linear-gradient(180deg,#9fb2c4 0%,#6c6656 50%,#3a3128 100%)"></div>
    <h3>Allies of Lantos</h3>
    <p>There are many variations of passages of Lorem Ipsum available, but the majority have suffered alteration in some form, by injected</p>
    <a class="btn-red">Read More</a>
  </article>
  <article class="card" style="left:439px">
    <div class="card-photo" role="img" aria-label="Small green sprout growing from dark soil" style="background:radial-gradient(circle at 50% 50%,#8aa05a 0%,#5b5b52 35%,#2e2e2c 100%)"></div>
    <h3>Potential Donors</h3>
    <p>There are many variations of passages of Lorem Ipsum available, but the majority have suffered alteration in some form, by injected</p>
    <a class="btn-red">Read More</a>
  </article>
  <article class="card" style="left:780px">
    <div class="card-photo" role="img" aria-label="Person standing on an open road at sunset" style="background:linear-gradient(180deg,#cfc08a 0%,#9a8b63 45%,#4a4a44 100%)"></div>
    <h3>Decision Makers</h3>
    <p>There are many variations of passages of Lorem Ipsum available, but the majority have suffered alteration in some form, by injected</p>
    <a class="btn-red">Read More</a>
  </article>
</section>

<section class="team" role="img" aria-label="Team hands joined together, tinted dark blue">
  <h2 class="sec-title">Meet the Team</h2>
  <p class="sec-lead">There are many variations of passages of Lorem Ipsum available, but the majority have suffered alteration in some form, by injected humour, or randomised words which don't look even slightly believable.</p>
  <svg class="team-arrow" style="left:96px" viewBox="0 0 20 40"><path d="M15 6L5 20l10 14" fill="none" stroke="#fff" stroke-width="3"/></svg>
  <svg class="team-arrow" style="left:1084px" viewBox="0 0 20 40"><path d="M5 6l10 14L5 34" fill="none" stroke="#fff" stroke-width="3"/></svg>

  <div class="member" style="left:218px;top:188px;width:180px">
    <div class="member-photo" role="img" aria-label="Portrait of board member" style="width:156px;height:156px;background:linear-gradient(180deg,#5a7fd0,#2d4c9a)"></div>
    <div class="member-name">Dorian L</div>
    <div class="member-role">Adventure</div>
  </div>
  <div class="member" style="left:490px;top:188px;width:220px">
    <div class="member-photo" role="img" aria-label="Portrait of board member" style="width:196px;height:196px;background:linear-gradient(180deg,#b8bcc0,#7b8086)"></div>
    <div class="member-name">Dorian L</div>
    <div class="member-role">Adventure</div>
  </div>
  <div class="member" style="left:798px;top:188px;width:180px">
    <div class="member-photo" role="img" aria-label="Portrait of board member" style="width:156px;height:156px;background:linear-gradient(180deg,#5a5e66,#2c2f36)"></div>
    <div class="member-name">Dorian L</div>
    <div class="member-role">Adventure</div>
  </div>
</section>

<footer>
  <div class="footer-col" style="left:98px">
    <h4>Our Link</h4>
    <ul><li>About us</li><li>Our work</li><li>Donate</li><li>Meet the team</li><li>Haiti's assets</li></ul>
  </div>
  <div class="footer-col" style="left:329px">
    <h4>Featured</h4>
    <ul><li>Hockey</li><li>Base Ball</li><li>Soccer</li><li>Basket ball</li><li>Soft Ball</li></ul>
  </div>
  <div class="footer-col contact" style="left:551px">
    <h4>Contact</h4>
    <ul>
      <li>( 03 ) 123 456 7895 ( Office )</li>
      <li>( 03 ) 123 456 7895 ( Cell )</li>
      <li>ugp@kelvoracommunitytrust.com</li>
      <li style="border-bottom:0"># 124 Our Street Name,<br>P.O. Box 00123. Our City,<br>dummy text of the printing</li>
    </ul>
  </div>
  <div class="footer-col newsletter" style="left:806px">
    <h4>Newsletter Signup</h4>
    <p>There are many variations of passages of Lorem Ipsum available, but the majority have suffered</p>
    <div class="signup"><div class="field">Email Addres</div><div class="send"><svg width="16" height="16" viewBox="0 0 16 16"><path d="M1 8l14-7-4 14-3-5z" fill="#fff"/></svg></div></div>
    <div class="social"><span style="background:#3b5a9a"></span><span style="background:#2aa3ef"></span><span style="background:#d34836"></span></div>
  </div>

  <div class="bottom-bar">
    <div class="copy">Copyright © 2016. kelvoracommunitytrust.com</div>
    <nav><span>Terms of Use</span><span>Legal disclaimer</span><span>Privacy Policy</span><span>Support</span><span>Sitemap</span></nav>
  </div>
</footer>

</body>
</html>
```